Business Card Design

I need a business card for company that is a limited company that was originally an off-road vehicle company (atv's side by sides snowmobiles and motorcycles) and I have recently sold the assets of the company that was operating under a different name and have become semi retired. I continue to do maintenance on these types of vehicles and also sell and install parts and accessories. Recently I have also contracted to a snowmobile club to operate their groomer to groom the snowmobile trails. I would like bright and bold colors.
Industry/Entity Type
Club
Contact Information for Business Card
KTV Holdings Ltd.
Milo Fenwick
780-413-2769

```html
<!DOCTYPE html>
<html lang="en">
<head>
<meta charset="utf-8">
<title>KTV Holdings Ltd. – Business Card</title>
<link rel="stylesheet" href="https://fonts.googleapis.com/css2?family=Open+Sans:wght@600;700&display=swap">
<style>
  :root {
    --backdrop: #5ccfbd;
    --card-stock: #dededc;
    --brand-blue: #1685cc;
    --ink: #2b2b2b;
    --logo-ink: #111111;
    --white: #ffffff;
  }
  * { box-sizing: border-box; margin: 0; padding: 0; }
  html, body {
    width: 1200px;
    height: 949px;
    overflow: hidden;
    background: var(--backdrop);
    font-family: "Open Sans", Arial, sans-serif;
  }
  .sheet {
    position: relative;
    width: 1200px;
    height: 949px;
    display: flex;
    align-items: center;
    justify-content: center;
    gap: 40px;
  }
  .card {
    position: relative;
    width: 540px;
    height: 309px;
    background: var(--card-stock);
    overflow: hidden;
    box-shadow: 0 6px 18px rgba(0, 0, 0, 0.18);
  }

  /* Front: name band and trade credentials */
  .name-band {
    position: absolute;
    left: 0;
    right: 0;
    top: 88px;
    height: 66px;
    background: var(--brand-blue);
    display: flex;
    align-items: center;
    padding-left: 42px;
  }
  .person-name {
    color: var(--white);
    font-weight: 600;
    font-size: 42px;
    letter-spacing: 1.5px;
  }
  .credentials {
    position: absolute;
    left: 104px;
    top: 170px;
    list-style: none;
    color: var(--ink);
    font-weight: 600;
    font-size: 14px;
    line-height: 1.55;
    letter-spacing: 0.4px;
  }

  /* Back: company name and contact band */
  .top-stripe {
    position: absolute;
    left: 0;
    right: 0;
    top: 0;
    height: 30px;
    background: var(--brand-blue);
  }
  .company-name {
    position: absolute;
    left: 0;
    right: 0;
    top: 100px;
    text-align: center;
    color: var(--logo-ink);
    font-weight: 700;
    font-size: 42px;
    letter-spacing: 1px;
  }
  .contact-band {
    position: absolute;
    left: 0;
    right: 0;
    bottom: 0;
    height: 64px;
    background: var(--brand-blue);
    display: flex;
    align-items: center;
    justify-content: space-between;
    padding: 0 26px;
    color: var(--white);
    font-weight: 600;
    font-size: 16px;
    letter-spacing: 0.5px;
  }
</style>
</head>
<body>
  <main class="sheet">
    <section class="card card-front" aria-label="Business card front">
      <div class="name-band">
        <h1 class="person-name">Milo Fenwick</h1>
      </div>
      <ul class="credentials">
        <li>Journeyman Red Seal Automotive Technician</li>
        <li>Journeyman Red Seal Motorcycle Technician</li>
        <li>Journeyman Parts Man</li>
      </ul>
    </section>

    <section class="card card-back" aria-label="Business card back">
      <div class="top-stripe"></div>
      <h2 class="company-name">KTV Holdings Ltd.</h2>
      <div class="contact-band">
        <span class="phone">780-413-2769</span>
        <span class="email">ktvhold.77@northmail.ca</span>
      </div>
    </section>
  </main>
</body>
</html>
```